ecommerce website design for pool store

I need a homepage designed for an e-commerce store for a pool shop. It will be similar to https://www.aquabrite.com.au/ but not an exact copy (ie. the icons, photos and colour scheme need to be different). aquabrite.com.au is one of our competitors but we love everything about their website.
I have attached the logo for this site. We want the background to be white and the colours used on the site to be the blue from the logo and the blue and green used on www.hopscotchyouth.com.au
I want the same layout for the logo, search and menu bar at the top along with the 'shop filter cartidges' feature button
Under that a similar slideshow
Under that, the categories with the logos, the best sellers, trending now (but call this 'latest products') and all the other same elements as on this example site.

```html
<!DOCTYPE html>
<html lang="en">
<head>
<meta charset="utf-8">
<title>Clearwater Pool Store</title>
<link href="https://fonts.googleapis.com/css2?family=Poppins:wght@400;500;600;700;800;900&family=Yellowtail&display=swap" rel="stylesheet">
<style>
:root{
  --sky:#0f9be0;
  --navy:#2e3192;
  --ink:#111318;
  --text:#555a66;
  --line:#e6e8ee;
  --soft:#f4f5f7;
  --card:#f3f3f5;
}
*{box-sizing:border-box;margin:0;padding:0}
html,body{width:1200px;height:3697px;overflow:hidden;background:#fff;font-family:'Poppins',sans-serif;color:var(--ink)}
.page{position:relative;width:1200px;height:3697px}
.abs{position:absolute}
.logo-badge{position:absolute;border-radius:50%;background:#fff;border:3px solid var(--navy);display:flex;align-items:center;justify-content:center;text-align:center;color:var(--navy);font-weight:600;font-size:12px;line-height:1.3;letter-spacing:1px}
.search{left:291px;top:47px;width:520px;height:42px;border:1px solid var(--line);border-radius:21px;display:flex;align-items:center;background:#fff}
.search .cat{width:68px;height:100%;background:var(--soft);border-radius:21px 0 0 21px;font-size:11px;display:flex;align-items:center;justify-content:center;gap:8px}
.search .ph{flex:1;padding-left:16px;font-size:11px;color:#aab}
.search .go{width:44px;height:44px;border-radius:50%;background:var(--sky);margin-right:-2px;display:flex;align-items:center;justify-content:center}
.cart{left:840px;top:56px;font-size:12px;display:flex;align-items:center;gap:6px}
.btn{position:absolute;background:var(--sky);color:#fff;font-size:12px;font-weight:500;border-radius:22px;display:flex;align-items:center;justify-content:center}
.nav{left:0;top:122px;width:1200px;height:50px;background:var(--soft)}
.nav span{position:absolute;top:16px;font-size:11px;transform:translateX(-50%)}
.hero{left:0;top:172px;width:1200px;height:468px;background:linear-gradient(90deg,#b98a5a 0%,#d7a77a 25%,#3d8a4e 45%,#2e7a44 60%,#1ea0c8 75%,#27b5e0 100%);overflow:hidden}
.hero-disc{left:384px;top:190px;width:432px;height:432px;border-radius:50%;background:rgba(14,20,24,.9);text-align:center;color:#fff}
.hero-disc .kick{margin-top:80px;font-size:28px;font-weight:500}
.hero-disc .script{font-family:'Yellowtail',cursive;font-size:92px;line-height:1;margin-top:4px;white-space:nowrap}
.hero-disc p{font-size:13px;line-height:27px;margin-top:14px}
.panel{position:absolute;top:733px;width:470px;height:382px;border:2px solid var(--sky);border-radius:22px;background:#fff}
.panel.navy{border-color:var(--navy)}
.row{position:absolute;left:50px;width:380px;height:80px;display:flex;align-items:center;gap:22px;border-bottom:1px solid var(--line);font-size:18px;font-weight:500;white-space:nowrap}
.row:last-child{border-bottom:none}
.row .ic{width:64px;height:64px;border-radius:50%;flex:none}
.section-title{position:absolute;left:108px;font-size:29px;font-weight:800;letter-spacing:-.5px}
.rule{position:absolute;height:2px;background:var(--soft)}
.arrow{position:absolute;width:28px;height:28px;border-radius:50%;display:flex;align-items:center;justify-content:center}
.card{position:absolute;width:224px;height:299px;background:var(--card);border-radius:10px;border:1px solid var(--line)}
.card.hot{background:var(--sky);border-color:var(--sky);color:#fff}
.card .tag{position:absolute;left:22px;top:16px;background:var(--navy);color:#fff;font-size:10px;padding:2px 9px;border-radius:10px}
.card.hot .tag{background:#fff;color:var(--ink)}
.card .photo{position:absolute;left:42px;top:72px;width:140px;height:120px;border-radius:14px}
.card .label{position:absolute;left:24px;bottom:14px;display:flex;align-items:center;gap:12px;font-size:11px;white-space:nowrap}
.card .label b{font-weight:600}
.card .label .sep{width:1px;height:14px;background:currentColor;opacity:.5}
.offer{left:0;top:2184px;width:1200px;height:749px;background:#f7f7f8}
.offer h2{position:absolute;left:105px;top:135px;font-size:48px;font-weight:900;letter-spacing:.5px}
.offer .lead{position:absolute;left:105px;top:225px;width:450px;font-size:13px;line-height:27px;color:var(--text)}
.tick{position:absolute;left:104px;width:58px;height:58px;border-radius:50%;background:var(--sky);display:flex;align-items:center;justify-content:center}
.offer h3{position:absolute;left:198px;font-size:21px;font-weight:500}
.offer .sub{position:absolute;left:198px;font-size:13px;line-height:27px;color:var(--text);width:400px}
.brand{position:absolute;top:3020px;font-size:20px;font-weight:700;color:var(--navy);transform:translateX(-50%)}
.foot-h{position:absolute;top:3262px;font-size:13px;font-weight:500}
.foot-l{position:absolute;font-size:11px;color:var(--text)}
.social{position:absolute;top:3480px;width:28px;height:28px;border-radius:50%;background:var(--sky)}
.pay{position:absolute;top:3450px;font-size:14px;font-weight:600;color:var(--navy)}
</style>
</head>
<body>
<div class="page">

  <div class="logo-badge" style="left:110px;top:30px;width:120px;height:120px;box-shadow:0 0 0 8px #fff">CLEARWATER<br>POOL STORE</div>
  <div class="abs search">
    <div class="cat">All <svg width="8" height="6"><path d="M1 1l3 3 3-3" stroke="#333" fill="none"/></svg></div>
    <div class="ph">Search items...</div>
    <div class="go"><svg width="20" height="20"><circle cx="8" cy="8" r="6" stroke="#fff" stroke-width="2" fill="none"/><path d="M12.5 12.5l5 5" stroke="#fff" stroke-width="2"/></svg></div>
  </div>
  <div class="abs cart">Cart
    <svg width="28" height="24"><path d="M2 3h4l3 12h13l3-9H7" stroke="#333" stroke-width="1.5" fill="none"/><circle cx="11" cy="19" r="2" fill="#333"/><circle cx="20" cy="19" r="2" fill="#333"/><circle cx="24" cy="4" r="4" fill="var(--sky)"/></svg>
  </div>
  <div class="btn" style="left:926px;top:47px;width:176px;height:41px">Shop Filter Cartidges</div>

  <nav class="abs nav">
    <span style="left:346px">Pumps</span><span style="left:416px">Filters</span><span style="left:499px">Chlorinators</span><span style="left:594px">Cleaners</span><span style="left:669px">Lights</span><span style="left:755px">Maintenance</span><span style="left:843px">Covers</span><span style="left:918px">Heaters</span><span style="left:987px">Spas</span><span style="left:1068px">Chemicals</span>
  </nav>

  <section class="abs hero" role="img" aria-label="Resort pool with sun loungers, umbrellas and palm trees"></section>
  <div class="abs hero-disc">
    <div class="kick">Buy Online</div>
    <div class="script">Pool Store</div>
    <p>Lorem ipsum dolor sit amet, consectetur adipiscing elit.<br>Maecenas dignissim tempor libero, sit amet</p>
  </div>
  <div class="btn" style="left:511px;top:512px;width:176px;height:38px;font-size:11px">Shop Filter Cartidges</div>

  <div class="panel" style="left:110px">
    <div class="row" style="top:35px"><div class="ic" style="background:radial-gradient(circle,#3b6fd0,#1a7fc8)" role="img" aria-label="Above ground pool"></div>Pools come with questions</div>
    <div class="row" style="top:115px"><div class="ic" style="background:radial-gradient(circle,#cfc6b6,#3aa0d8)" role="img" aria-label="Spa tub"></div>Well, backed by 20 years</div>
    <div class="row" style="top:195px"><div class="ic" style="background:radial-gradient(circle,#6f6f74,#2a9ad8)" role="img" aria-label="Spa cover"></div>Experience and an honest,</div>
    <div class="row" style="top:275px"><div class="ic" style="background:radial-gradient(circle,#174a3c,#1aa3e8)" role="img" aria-label="Diving kit"></div>Our friendly team of pool</div>
  </div>
  <div class="panel navy" style="left:637px">
    <div class="row" style="top:35px"><div class="ic" style="background:radial-gradient(circle,#7a8ab0,#2e3192)" role="img" aria-label="Water pump handle"></div>We want to make this</div>
    <div class="row" style="top:115px"><div class="ic" style="background:radial-gradient(circle,#e8eaf2,#2e3192)" role="img" aria-label="Sun lounger"></div>Super-easy for you, so all our</div>
    <div class="row" style="top:195px"><div class="ic" style="background:radial-gradient(circle,#8a8a90,#2e3192)" role="img" aria-label="Pool slide"></div>Products come with a</div>
    <div class="row" style="top:275px"><div class="ic" style="background:radial-gradient(circle,#9ab8e0,#2e3192)" role="img" aria-label="Chlorine dispensers"></div>60-day trial period.</div>
  </div>

  <h2 class="section-title" style="top:1203px">BEST SELERS</h2>
  <div class="rule" style="left:312px;top:1222px;width:710px"></div>
  <div class="arrow" style="left:1048px;top:1208px;background:var(--sky)"><svg width="8" height="10"><path d="M6 1L2 5l4 4" stroke="#fff" fill="none" stroke-width="1.5"/></svg></div>
  <div class="arrow" style="left:1080px;top:1208px;background:var(--navy)"><svg width="8" height="10"><path d="M2 1l4 4-4 4" stroke="#fff" fill="none" stroke-width="1.5"/></svg></div>

  <div class="card" style="left:102px;top:1290px"><span class="tag">New</span><div class="photo" role="img" aria-label="Water pump handle" style="background:linear-gradient(135deg,#3a4b9a,#c9ccd6)"></div><div class="label"><svg width="24" height="20"><path d="M1 2h4l3 11h12l2-8H6" stroke="currentColor" stroke-width="1.4" fill="none"/><circle cx="10" cy="17" r="1.6" fill="currentColor"/><circle cx="18" cy="17" r="1.6" fill="currentColor"/></svg><span class="sep"></span><span><b>Water Pump</b> - $79.99</span></div></div>
  <div class="card hot" style="left:356px;top:1290px"><span class="tag">New</span><div class="photo" role="img" aria-label="White sun lounger" style="background:linear-gradient(135deg,#e9f2fa,#7cc6ee)"></div><div class="label"><svg width="24" height="20"><path d="M1 2h4l3 11h12l2-8H6" stroke="currentColor" stroke-width="1.4" fill="none"/><circle cx="10" cy="17" r="1.6" fill="currentColor"/><circle cx="18" cy="17" r="1.6" fill="currentColor"/></svg><span class="sep"></span><span><b>Relax Chair - $79.99</b></span></div></div>
  <div class="card" style="left:611px;top:1290px"><span class="tag">New</span><div class="photo" role="img" aria-label="Fins and snorkel mask" style="background:linear-gradient(135deg,#1a5b4c,#35c0b0)"></div><div class="label"><svg width="24" height="20"><path d="M1 2h4l3 11h12l2-8H6" stroke="currentColor" stroke-width="1.4" fill="none"/><circle cx="10" cy="17" r="1.6" fill="currentColor"/><circle cx="18" cy="17" r="1.6" fill="currentColor"/></svg><span class="sep"></span><span><b>Diving Kit</b> - $79.99</span></div></div>
  <div class="card" style="left:868px;top:1290px"><span class="tag">New</span><div class="photo" role="img" aria-label="Floating chlorine dispensers" style="background:linear-gradient(135deg,#1f6fd0,#c8a070)"></div><div class="label"><svg width="24" height="20"><path d="M1 2h4l3 11h12l2-8H6" stroke="currentColor" stroke-width="1.4" fill="none"/><circle cx="10" cy="17" r="1.6" fill="currentColor"/><circle cx="18" cy="17" r="1.6" fill="currentColor"/></svg><span class="sep"></span><span><b>Plastic Caps</b>- $79.99</span></div></div>

  <h2 class="section-title" style="top:1685px">LATEST PRODUCTS</h2>
  <div class="rule" style="left:405px;top:1704px;width:617px"></div>
  <div class="arrow" style="left:1048px;top:1690px;background:var(--sky)"><svg width="8" height="10"><path d="M6 1L2 5l4 4" stroke="#fff" fill="none" stroke-width="1.5"/></svg></div>
  <div class="arrow" style="left:1080px;top:1690px;background:var(--navy)"><svg width="8" height="10"><path d="M2 1l4 4-4 4" stroke="#fff" fill="none" stroke-width="1.5"/></svg></div>

  <div class="card" style="left:102px;top:1767px"><span class="tag">New</span><div class="photo" role="img" aria-label="Round grey spa cover" style="background:linear-gradient(135deg,#5f5f66,#a9a9b0)"></div><div class="label"><svg width="24" height="20"><path d="M1 2h4l3 11h12l2-8H6" stroke="currentColor" stroke-width="1.4" fill="none"/><circle cx="10" cy="17" r="1.6" fill="currentColor"/><circle cx="18" cy="17" r="1.6" fill="currentColor"/></svg><span class="sep"></span><span><b>Water Pump</b> - $79.99</span></div></div>
  <div class="card" style="left:356px;top:1767px"><span class="tag">New</span><div class="photo" role="img" aria-label="Spa tub" style="background:linear-gradient(135deg,#d9d2c2,#9b8f78)"></div><div class="label"><svg width="24" height="20"><path d="M1 2h4l3 11h12l2-8H6" stroke="currentColor" stroke-width="1.4" fill="none"/><circle cx="10" cy="17" r="1.6" fill="currentColor"/><circle cx="18" cy="17" r="1.6" fill="currentColor"/></svg><span class="sep"></span><span><b>Water Pump</b> - $79.99</span></div></div>
  <div class="card" style="left:611px;top:1767px"><span class="tag">New</span><div class="photo" role="img" aria-label="Inflatable above ground pool" style="background:linear-gradient(135deg,#1c3f9e,#3fa8e8)"></div><div class="label"><svg width="24" height="20"><path d="M1 2h4l3 11h12l2-8H6" stroke="currentColor" stroke-width="1.4" fill="none"/><circle cx="10" cy="17" r="1.6" fill="currentColor"/><circle cx="18" cy="17" r="1.6" fill="currentColor"/></svg><span class="sep"></span><span><b>Diving Kit</b> - $79.99</span></div></div>
  <div class="card" style="left:868px;top:1767px"><span class="tag">New</span><div class="photo" role="img" aria-label="Grey spiral pool slide" style="background:linear-gradient(135deg,#6e6e74,#b8b8be)"></div><div class="label"><svg width="24" height="20"><path d="M1 2h4l3 11h12l2-8H6" stroke="currentColor" stroke-width="1.4" fill="none"/><circle cx="10" cy="17" r="1.6" fill="currentColor"/><circle cx="18" cy="17" r="1.6" fill="currentColor"/></svg><span class="sep"></span><span><b>Plastic Caps</b>- $79.99</span></div></div>

  <section class="abs offer">
    <h2>WHAT WE OFFER</h2>
    <p class="lead">Lorem ipsum dolor sit amet, consectetur adipiscing elit. Maecenas dignissim tempor libero, sit amet obortis dolor. Morbi porta mauris eget ipsum auctor</p>
    <div class="tick" style="top:363px"><svg width="26" height="20"><path d="M2 10l8 8L24 2" stroke="#fff" stroke-width="2.5" fill="none"/></svg></div>
    <h3 style="top:372px">Lifetime After-sales</h3>
    <p class="sub" style="top:422px">Lorem ipsum dolor sit amet, consectetur adipiscing elit. Maecenas dignissim tempor libero</p>
    <div class="tick" style="top:511px"><svg width="26" height="20"><path d="M2 10l8 8L24 2" stroke="#fff" stroke-width="2.5" fill="none"/></svg></div>
    <h3 style="top:522px">Game-changing Value</h3>
    <p class="sub" style="top:572px">Lorem ipsum dolor sit amet, consectetur adipiscing elit. Maecenas dignissim tempor libero</p>
    <div class="abs" style="left:729px;top:108px;width:359px;height:498px;border:2px solid var(--sky);border-radius:6px"></div>
    <div class="abs" role="img" aria-label="Pool edge with ladder rails over clear blue water" style="left:696px;top:134px;width:362px;height:499px;border-radius:6px;background:linear-gradient(120deg,#1b8fe0 0%,#3cb0f0 55%,#e6dccb 62%,#f2ece0 100%)"></div>
  </section>

  <div class="brand" style="left:197px">Marlin</div>
  <div class="brand" style="left:392px">Tidecraft</div>
  <div class="brand" style="left:584px;font-weight:400;color:#444">Poolbloom</div>
  <div class="brand" style="left:786px">Coralwave</div>
  <div class="brand" style="left:982px">Aquaforge</div>

  <div class="abs" style="left:0;top:3142px;width:1200px;height:6px;background:var(--sky)"></div>

  <div class="logo-badge" style="left:110px;top:3226px;width:120px;height:120px">CLEARWATER<br>POOL STORE</div>
  <p class="foot-l" style="left:115px;top:3378px;font-size:13px;line-height:26px;width:200px">Lorem ipsum dolor sit amet, consectetur adipiscing elit. Maecenas</p>
  <div class="social" style="left:112px"></div>
  <div class="social" style="left:147px;background:var(--navy)"></div>
  <div class="social" style="left:183px"></div>
  <div class="social" style="left:217px"></div>

  <div class="foot-h" style="left:436px">Useful Links</div>
  <div class="foot-l" style="left:436px;top:3312px">Pumps</div>
  <div class="foot-l" style="left:436px;top:3341px">Filters</div>
  <div class="foot-l" style="left:436px;top:3370px">Chlorinators</div>
  <div class="foot-l" style="left:436px;top:3398px">Cleaners</div>
  <div class="foot-l" style="left:436px;top:3428px">Lights</div>
  <div class="foot-l" style="left:436px;top:3457px">Maintenance</div>
  <div class="foot-l" style="left:620px;top:3312px">Covers</div>
  <div class="foot-l" style="left:620px;top:3341px">Heaters</div>
  <div class="foot-l" style="left:620px;top:3370px">Spas</div>
  <div class="foot-l" style="left:620px;top:3398px">Chemicals</div>

  <div class="foot-h" style="left:812px">Contact Details</div>
  <svg class="abs" style="left:810px;top:3310px" width="14" height="16"><path d="M7 15s5-5 5-9A5 5 0 0 0 2 6c0 4 5 9 5 9z" stroke="var(--sky)" fill="none"/><circle cx="7" cy="6" r="2" stroke="var(--sky)" fill="none"/></svg>
  <div class="foot-l" style="left:831px;top:3310px;line-height:18px">48 Harbour Lane, Suite B<br>Seaview, CA 90210</div>
  <svg class="abs" style="left:810px;top:3363px" width="14" height="14"><path d="M3 1l3 3-2 2a8 8 0 0 0 4 4l2-2 3 3-2 2C6 13 1 8 1 3z" stroke="var(--sky)" fill="none"/></svg>
  <div class="foot-l" style="left:831px;top:3362px">(92) 555 010 2233</div>
  <svg class="abs" style="left:809px;top:3382px" width="15" height="11"><rect x="1" y="1" width="13" height="9" stroke="var(--sky)" fill="none"/><path d="M1 1l6.5 5L14 1" stroke="var(--sky)" fill="none"/></svg>
  <div class="foot-l" style="left:831px;top:3380px">hello@clearwaterpools.com</div>

  <div class="pay" style="left:806px">Zelmo</div>
  <div class="pay" style="left:864px">Tarvia</div>
  <div class="pay" style="left:928px">Quenta</div>
  <div class="pay" style="left:1002px">Pebblo</div>

  <div class="abs" style="left:0;top:3588px;width:1200px;height:1px;background:var(--line)"></div>
  <p class="abs" style="left:0;top:3630px;width:1200px;text-align:center;font-size:11px;color:var(--text)">© 2022, <b style="color:var(--ink);font-weight:500">Clearwater Pool Store.</b> All Rights Reserved.</p>

</div>
</body>
</html>
```